Funk up our website

Our website is currently in operation and working well, see it at www.clearbriefhub.co.uk

However it needs some redesign work, to help it feel fresh, inviting and friendly.

We need graphic mockups (png hi-res) to pass to the dev team, to do the css work:

homepage - http://www.clearbriefhub.co.uk
topic page - http://www.clearbriefhub.co.uk/guidance/business
sub-topic - http://www.clearbriefhub.co.uk/guidance/business/goods-services
content - http://www.clearbriefhub.co.uk/guidance/business/goods-services/heads-of-terms
ancillary pages - contact us, heads of terms, etc

The structure of the page in terms of the placement of header, menu bar, content area and footer needs to remain, but the design of it is up for grabs.

The site is currently free to use, but in the future will have the aim of getting users to register for free, but with the option of buying documents on an individual basis, or subscription basis, or subscribing to additional legal services.

Additional information
---------------------------
Users
1. Owners and managers in small and medium businesses
2. In the UK only
3. Who find dealing with legal issues and lawyers intimidating
4. Who are searching for online help to try and avoid having to deal with a lawyer
5. Or have been referred via social media
Desired user experience
1. A welcoming, friendly site
2. That takes the complexity out of dealing with legal issues
3. That really does clear the brief
4. That is fast, efficient and clear
5. That is pleasantly different from the normal experience of interacting with a law firm
Relevant factors
1. Most visitors will first land on a content page (e.g. [link]) via a search result or banner advertisement – not the Home Page
2. Repeat visitors are more likely to go to the Home Page
3. Works with web responsive design techniques for display on smartphones and tablets
4. Implemented through CSS
Colour palette
Designer should feel able to build the palette around the following core colours
CMYK
YELLOW = 0,25,100,0
GREEN = 80,0,100,0
BLUE = 100,25,0,0

RGB
YELLOW = 255,195,15
GREEN = 15,175,75
BLUE = 0,140,210

PANTONE
YELLOW = 123c
GREEN = 361c
BLUE = 3005c

Fonts
Soho Gothic, Soho, Arial
Designer should feel able to add fonts to complement these core fonts.

Our logo needs to remain (see attached document) Our strap line, can be changed if needed.

Best
RK
Updates

Hi All

Some websites worth having a look at for how people have done things differently / added something distinctive to their website:

http://www.brevicounsel.co.uk/
https://www.tandelegal.co.uk/
http://www.quillatrix.com/

Cheers
RK

Hi All

Thanks for your designs. Just back in the office today, we will discuss and feedback / decide asap.

Best
RK

```html
<!DOCTYPE html>
<html lang="en">
<head>
<meta charset="utf-8">
<title>Clear Brief Hub – Why protect business information?</title>
<link href="https://fonts.googleapis.com/css2?family=Arimo:wght@400;700&display=swap" rel="stylesheet">
<style>
:root{
  --yellow:#ffc30f;
  --green:#0faf4b;
  --link-green:#0e9a3f;
  --blue:#008cd2;
  --name-blue:#0a7cb8;
  --ink:#111;
  --text:#444;
  --muted:#666;
  --nav:#c3c3c3;
  --page:#efefef;
  --panel:#e8e8e8;
  --orange:#f7a200;
}
*{box-sizing:border-box;margin:0;padding:0}
html,body{width:1200px;height:1100px;overflow:hidden}
body{font-family:"Arimo",Arial,sans-serif;color:var(--text);background:linear-gradient(#f7f7f7,#ececec);position:relative}
a{text-decoration:none;color:inherit}
.abs{position:absolute}

/* header */
.site-header{position:absolute;left:0;top:0;width:1200px;height:114px;background:#fff;border-bottom:1px solid #e2e2e2}
.brand{position:absolute;left:103px;top:28px;display:flex;align-items:center;gap:14px}
.brand-mark{width:72px;height:70px;background:var(--green);border-radius:4px}
.brand-name{font-weight:700;font-size:36px;line-height:32px;color:var(--ink);letter-spacing:-1px}
.search{position:absolute;left:642px;top:19px;width:236px;height:27px;border:1px solid #bbb;border-radius:14px;overflow:hidden;display:flex;background:#fff}
.search-field{flex:1;display:flex;align-items:center;gap:6px;padding-left:12px;font-size:14px;color:#777}
.search-btn{width:64px;background:var(--orange);color:#fff;font-size:11px;font-weight:700;display:flex;align-items:center;justify-content:center}
.account{position:absolute;left:890px;top:27px;font-size:11px;color:#555;letter-spacing:.3px}
.account .sep{color:var(--blue);margin:0 6px}
.social{position:absolute;top:20px;width:24px;height:24px;border-radius:50%}
.main-nav{position:absolute;top:64px;left:483px;display:flex;gap:2px}
.main-nav a{height:34px;background:var(--nav);color:#fff;font-size:12px;letter-spacing:.4px;display:flex;align-items:center;justify-content:center;border-radius:4px}

/* breadcrumb */
.breadcrumb{position:absolute;left:0;top:115px;width:1200px;height:30px;background:#eaeaea;font-size:11px;color:#555;padding:8px 0 0 110px}
.breadcrumb .current{color:var(--link-green)}

/* share bar */
.share{position:absolute;left:0;width:48px;height:48px;display:flex;align-items:center;justify-content:center}

/* content */
.section-title{position:absolute;left:112px;top:172px;font-size:25px;color:var(--ink)}
.topic-bar{position:absolute;left:112px;top:206px;width:640px;height:36px;background:linear-gradient(var(--blue),#0a9ee4);border-radius:0 6px 0 0;color:#fff;font-size:18px;font-weight:700;padding:8px 0 0 18px}
.article{position:absolute;left:130px;top:270px;width:500px;font-size:12px;line-height:16px}
.lead{font-weight:700;font-size:13px;line-height:16px;color:#444;margin-bottom:16px}
.bullets{list-style:none;margin-bottom:17px}
.bullets li{position:relative;padding-left:13px;margin-bottom:3px}
.bullets li::before,.links li::before{content:"";position:absolute;left:2px;top:4px;border-left:5px solid var(--green);border-top:4px solid transparent;border-bottom:4px solid transparent}
.subhead{font-weight:700;margin-bottom:16px}
.related{position:absolute;left:112px;top:553px;width:638px;height:321px;background:var(--panel);border-top:2px solid var(--green);border-bottom:2px solid var(--green);padding:28px 30px}
.related h3{font-size:17px;color:var(--ink);margin-bottom:6px}
.links{list-style:none;margin-bottom:20px}
.links li{position:relative;padding-left:14px;font-size:12px;font-weight:700;color:var(--link-green);line-height:24px}
.links li::before{top:8px}

/* sidebar */
.help-title{position:absolute;left:769px;top:172px;font-size:25px;color:var(--ink)}
.finder{position:absolute;left:769px;top:206px;width:319px;height:258px;background:var(--yellow);border-radius:8px;padding:24px 26px;font-size:12px;color:#222}
.finder p{line-height:16px}
.finder label.big{display:block;font-size:17px;font-weight:700;margin:14px 0 4px;color:#111}
.finder .input{width:263px;height:25px;background:#fff;border:1px solid #d9a200}
.check{display:flex;align-items:center;gap:6px;margin-top:13px;padding-left:4px}
.box{width:12px;height:12px;background:#fff;border:1px solid #888}
.badge{width:14px;height:12px;border-radius:2px}
.finder .go{margin-top:14px;width:123px;height:38px;background:linear-gradient(#3a3a3a,#050505);border-radius:3px;color:#fff;font-size:14px;font-weight:700;display:flex;align-items:center;justify-content:center}
.advisers{position:absolute;left:769px;top:477px;width:319px;height:497px;background:#f9f9f9;border-radius:8px;padding:24px 26px}
.advisers h2{font-size:17px;color:var(--ink);margin-bottom:16px}
.adviser{display:flex;align-items:center;height:61px;border-bottom:1px solid #ddd;position:relative}
.adviser:last-child{border-bottom:none}
.photo{width:33px;height:33px;background:linear-gradient(#d8cfc4,#8a7a6c);margin-right:11px}
.adviser .name{font-size:13px;font-weight:700;color:var(--name-blue)}
.adviser .firm{font-size:11px;color:#222;margin-top:3px}
.adviser .mark{position:absolute;right:2px;top:24px;width:16px;height:14px;border-radius:2px}
.mark.member{background:var(--green)}
.mark.partner{background:#4b6f95}

.feedback{position:absolute;left:1168px;top:360px;width:32px;height:100px;background:var(--green);border:2px solid #fff;border-right:none;color:#fff;font-size:16px;font-weight:700;writing-mode:vertical-rl;transform:rotate(180deg);display:flex;align-items:center;justify-content:center;box-shadow:0 0 0 1px var(--green)}

/* footer */
.footer-band{position:absolute;left:0;top:993px;width:1200px;height:15px;background:var(--yellow)}
.footer-nav{position:absolute;left:0;top:1008px;width:1200px;height:63px;background:#fff;display:flex;justify-content:center;align-items:center;font-size:12px;color:#444;letter-spacing:.3px}
.footer-nav .sep{color:var(--green);margin:0 10px}
.copyright{position:absolute;left:0;top:1071px;width:1200px;height:29px;background:var(--yellow);color:#fff;font-size:11px;padding:9px 0 0 110px}
</style>
</head>
<body>

<header class="site-header">
  <a class="brand" href="#"><span class="brand-mark"></span><span class="brand-name">Clear Brief<br>Hub</span></a>
  <div class="search">
    <div class="search-field">
      <svg width="15" height="15" viewBox="0 0 15 15"><circle cx="6" cy="6" r="4.5" fill="none" stroke="#6a8fb0" stroke-width="1.6"/><line x1="9.5" y1="9.5" x2="14" y2="14" stroke="#6a8fb0" stroke-width="2"/></svg>
      Search
    </div>
    <div class="search-btn">SEARCH</div>
  </div>
  <div class="account">REGISTER<span class="sep">|</span>LOGIN</div>
  <span class="social" style="left:1010px;background:#3b5590"></span>
  <span class="social" style="left:1042px;background:#2aa3df"></span>
  <span class="social" style="left:1074px;background:#2b7bb9"></span>
  <nav class="main-nav">
    <a href="#" style="width:75px">HOME</a>
    <a href="#" style="width:126px">GUIDE YOURSELF</a>
    <a href="#" style="width:126px">DRAFT YOURSELF</a>
    <a href="#" style="width:156px">SEARCH FOR A LAWYER</a>
    <a href="#" style="width:126px">GET YOUR DRAFTS</a>
  </nav>
</header>

<div class="breadcrumb">Home &gt;&nbsp; Guide Yourself &gt;&nbsp; Trade &amp; e-commerce &gt;&nbsp; <span class="current">Why protect business information?</span></div>

<div class="share" style="top:202px;background:#3b5590"></div>
<div class="share" style="top:250px;background:#2aa3df"></div>
<div class="share" style="top:299px;background:#7e8e95">
  <svg width="22" height="15" viewBox="0 0 22 15"><rect x="1" y="1" width="20" height="13" fill="#fff"/><polyline points="1,1 11,9 21,1" fill="none" stroke="#7e8e95" stroke-width="1.6"/></svg>
</div>
<div class="share" style="top:348px;background:#8d989d">
  <svg width="20" height="18" viewBox="0 0 20 18"><rect x="5" y="0" width="10" height="5" fill="#fff"/><rect x="0" y="5" width="20" height="8" rx="2" fill="#fff"/><rect x="5" y="10" width="10" height="8" fill="#fff" stroke="#8d989d" stroke-width="1.4"/></svg>
</div>
<div class="share" style="top:397px;background:#f46a4e">
  <svg width="18" height="18" viewBox="0 0 18 18"><rect x="7" y="0" width="4" height="18" fill="#fff"/><rect x="0" y="7" width="18" height="4" fill="#fff"/></svg>
</div>

<main>
  <h1 class="section-title">Trade &amp; E-commerce</h1>
  <div class="topic-bar">Why protect business information?</div>
  <article class="article">
    <p class="lead">Your business is likely to hold valuable information that you wish to keep confi-<br>dential. For example:</p>
    <ul class="bullets">
      <li>Market-sensitive information;</li>
      <li>Customer lists and customer relationship management data;</li>
      <li>Technical knowledge;</li>
      <li>Trade secrets, such as an inventions; and</li>
      <li>Information about past, present and future employees, customers and suppliers.</li>
    </ul>
    <p class="subhead">Protecting information may:</p>
    <ul class="bullets">
      <li>Avoid exploitation by those who receive it outside the business and may wish to make a commercial gain out of it; and</li>
      <li style="margin-top:6px">Provide you with a means of compensation should a third party exploit it without permission.</li>
    </ul>
  </article>

  <section class="related">
    <h3>Relevant documents:</h3>
    <ul class="links"><li>Non-disclosure agreement</li></ul>
    <h3>Related issues:</h3>
    <ul class="links">
      <li>Making the most of your IP rights</li>
      <li>How can you protect your intellectual property?</li>
      <li>How do you put a non-disclosure agreement in place?</li>
      <li>When does the law protect business information?</li>
      <li>What is copyright?</li>
      <li>What is a patent?</li>
      <li>How do you protect your designs?</li>
    </ul>
  </section>
</main>

<aside>
  <h2 class="help-title">Need expert legal help?</h2>
  <form class="finder">
    <p>The lawyers listed below have experience in this area. Filter by postcode or by filter criteria.</p>
    <label class="big">Postcode:</label>
    <div class="input"></div>
    <div class="check" style="margin-top:14px"><span class="box"></span><span class="badge" style="background:#4b6f95"></span>LexCircle member</div>
    <div class="check"><span class="box"></span><span class="badge" style="background:var(--green)"></span>Fast, efficient &amp; clear</div>
    <div class="go">Search</div>
  </form>

  <section class="advisers">
    <h2>We can advise or help you draft</h2>
    <div class="adviser"><span class="photo" role="img" aria-label="Portrait of Clara Penhallow"></span><div><div class="name">Clara Penhallow</div><div class="firm">Harwood Solicitors</div></div><span class="mark member"></span></div>
    <div class="adviser"><span class="photo" role="img" aria-label="Portrait of Miriam Ashcombe"></span><div><div class="name">Miriam Ashcombe</div><div class="firm">Harwood Solicitors</div></div><span class="mark member"></span></div>
    <div class="adviser"><span class="photo" role="img" aria-label="Portrait of Louise Terrant"></span><div><div class="name">Louise Terrant</div><div class="firm">Harwood Solicitors</div></div><span class="mark member"></span></div>
    <div class="adviser"><span class="photo" role="img" aria-label="Portrait of Natalie Brisco"></span><div><div class="name">Natalie Brisco</div><div class="firm">Harwood Solicitors</div></div><span class="mark member"></span></div>
    <div class="adviser"><span class="photo" role="img" aria-label="Portrait of Nadia Orlova"></span><div><div class="name">Nadia Orlova</div><div class="firm">Brampton Hale &amp; Co Ltd</div></div><span class="mark partner"></span></div>
    <div class="adviser"><span class="photo" role="img" aria-label="Portrait of Ravi Mehtani"></span><div><div class="name">Ravi Mehtani</div><div class="firm">Harwood Solicitors</div></div><span class="mark member"></span></div>
    <div class="adviser"><span class="photo" role="img" aria-label="Portrait of Simon Aldgate"></span><div><div class="name">Simon Aldgate</div><div class="firm">Brampton Hale &amp; Co Ltd</div></div><span class="mark partner"></span></div>
  </section>
</aside>

<a class="feedback" href="#">feedback</a>

<footer>
  <div class="footer-band"></div>
  <nav class="footer-nav">
    CONTACT US<span class="sep">|</span>ABOUT US<span class="sep">|</span>TERMS AND CONDITIONS<span class="sep">|</span>PRIVACY POLICY<span class="sep">|</span>TERMINATE USER ACCOUNT<span class="sep">|</span>FAQS FOR USERS<span class="sep">|</span>IF YOU'RE A LAWYER
  </nav>
  <div class="copyright">© Northgate Legal Limited 2012</div>
</footer>

</body>
</html>
```